BRELLANDA EXTRA VIRGIN OLIVE OIL

I needs a design for an Australian Extra Virgin Olive Oil.

The label will go on a round clear bottle

The label size front and back is 145mm high x 60mm wide.

The important points for the design are as follows.

I want to see elegant olives on the label so that non English speaking markets can easily understand its olive oil. I want it too look classy . IT must also look Australian but I don't want to see kangaroos just colours that reflect Australia.

The mandatory info on front label will be

BRELLANDA

Cold Pressed
EXTRA VIRGIN OLIVE OIL

AUSTRALIAN

1 litre

```html
<!DOCTYPE html>
<html lang="en">
<head>
<meta charset="utf-8">
<title>Brellanda Extra Virgin Olive Oil – Front Label</title>
<link href="https://fonts.googleapis.com/css2?family=Cinzel:wght@700&family=Lato:wght@400&family=Lobster+Two:ital,wght@1,700&family=Pathway+Gothic+One&display=swap" rel="stylesheet">
<style>
  :root {
    --olive-deep: #4a5a16;
    --olive-dark: #5d6d1f;
    --olive-mid: #8a9433;
    --olive-wave: #b9bd5e;
    --cream-light: #f6f4c8;
    --cream-mid: #ecebae;
    --cream-text: #f3edc4;
    --ink-green: #4f5a12;
    --olive-fruit: #a6b83a;
    --leaf-green: #6f8a2a;
    --page: #ffffff;
  }
  html, body {
    margin: 0;
    padding: 0;
    width: 1200px;
    height: 2244px;
    overflow: hidden;
    background: var(--page);
  }
  .label {
    position: absolute;
    left: 308px;
    top: 132px;
    width: 780px;
    height: 1956px;
    border-radius: 390px;
    overflow: hidden;
  }
  .label-bg {
    position: absolute;
    inset: 0;
    width: 780px;
    height: 1956px;
  }
  .bottle-illustration {
    position: absolute;
    left: 170px;
    top: 40px;
    width: 440px;
    height: 480px;
    border-radius: 50% 50% 40% 40%;
    background: radial-gradient(ellipse at 50% 55%, rgba(150,160,60,0.85), rgba(120,135,45,0.55) 55%, rgba(93,109,31,0) 75%);
  }
  .olive-branch-illustration {
    position: absolute;
    left: 60px;
    top: 1230px;
    width: 700px;
    height: 420px;
    border-radius: 45%;
    background: radial-gradient(ellipse at 45% 50%, var(--olive-fruit), rgba(111,138,42,0.7) 50%, rgba(236,235,174,0) 75%);
  }
  .brand-name {
    position: absolute;
    left: 0; right: 0;
    top: 590px;
    margin: 0;
    text-align: center;
    font-family: "Cinzel", serif;
    font-weight: 700;
    font-size: 84px;
    letter-spacing: 1px;
    color: var(--cream-text);
  }
  .process {
    position: absolute;
    left: 0; right: 0;
    top: 700px;
    text-align: center;
    font-family: "Lato", sans-serif;
    font-size: 60px;
    color: var(--cream-text);
  }
  .grade {
    position: absolute;
    left: 62px;
    top: 900px;
    font-family: "Lobster Two", cursive;
    font-style: italic;
    font-weight: 700;
    font-size: 62px;
    color: var(--ink-green);
  }
  .product {
    position: absolute;
    left: 170px;
    top: 990px;
    margin: 0;
    font-family: "Pathway Gothic One", sans-serif;
    font-weight: 400;
    font-size: 196px;
    line-height: 1;
    color: var(--olive-dark);
    letter-spacing: 1px;
  }
  .origin {
    position: absolute;
    left: 0; right: 0;
    top: 1684px;
    text-align: center;
    font-family: "Cinzel", serif;
    font-weight: 700;
    font-size: 48px;
    color: var(--ink-green);
  }
  .volume {
    position: absolute;
    left: 0; right: 0;
    top: 1800px;
    text-align: center;
    font-family: "Lato", sans-serif;
    font-size: 84px;
    color: var(--cream-text);
  }
</style>
</head>
<body>
  <section class="label">
    <svg class="label-bg" viewBox="0 0 780 1956" aria-hidden="true">
      <defs>
        <linearGradient id="top-band" x1="0" y1="0" x2="0" y2="1">
          <stop offset="0" stop-color="#4f5f18"/>
          <stop offset="0.7" stop-color="#5d6d1f"/>
          <stop offset="1" stop-color="#7d8a2c"/>
        </linearGradient>
        <linearGradient id="cream-body" x1="0" y1="0" x2="0" y2="1">
          <stop offset="0" stop-color="#f6f4c8"/>
          <stop offset="1" stop-color="#e8e7a4"/>
        </linearGradient>
      </defs>
      <rect class="body-fill" x="0" y="0" width="780" height="1956" fill="url(#cream-body)"/>
      <path class="wave-light" d="M0 0 H780 V900 C620 960 420 860 250 880 C150 892 70 920 0 940 Z" fill="var(--olive-wave)"/>
      <path class="top-band" d="M0 0 H780 V860 C620 920 420 820 250 840 C150 852 70 880 0 900 Z" fill="url(#top-band)"/>
      <path class="bottom-band" d="M0 1770 C260 1745 520 1745 780 1770 V1956 H0 Z" fill="var(--olive-deep)"/>
    </svg>

    <div class="bottle-illustration" role="img" aria-label="Illustration of an oil bottle with an olive sprig"></div>

    <h1 class="brand-name">BRELLANDA</h1>
    <div class="process">Cold Pressed</div>

    <div class="grade">Extra Virgin Oil</div>
    <h2 class="product">OLIVE OIL</h2>

    <div class="olive-branch-illustration" role="img" aria-label="Illustration of a green olive branch with leaves and olives"></div>

    <div class="origin">AUSTRALIAN</div>
    <div class="volume">1 litre</div>
  </section>
</body>
</html>
```